New Business Card for Web Design/Internet Marketing Company

Looking for a great looking new business card. We are a 10 year old web design, internet marketing and website management company that works mostly with small businesses.

Our new card needs to better match the colors and style of our website, be bold, extremely usable and slightly edgy.

Target Market(s)

Small/Medium businesses that have websites

Industry/Entity Type

Internet

Requirements
Must have
• Front and back design, full color, rounded corners please

Must use the colors/style of our website (JPG provided)

INFO FOR CARDS (as readable as possible please)
Mark Pellow
President/CEO
mark@brightlanesites.com
Phone: 520-481-7093
Toll Free: 866-481-7093
Address: 4315 E. Kestrel Ave. Ste. 140, Tucson, AZ 85733

THINGS I WANT TO PROMOTE (if there is room):
1. Our Website - www.brightlanesites.com

2. Social Media
Twitter: @brightlanesites
Facebook: www.facebook.com/brightlanesites

3. Our Services
Web Design
Internet Marketing
Website Management

```html
<!DOCTYPE html>
<html lang="en">
<head>
<meta charset="utf-8">
<title>Bright Lane Sites – Business Card</title>
<link rel="stylesheet" href="https://fonts.googleapis.com/css2?family=Ubuntu:wght@400;500;700&display=swap">
<style>
  :root {
    --navy-deep: #26236a;
    --navy-mid: #1f3f92;
    --navy-glow: #1c56a8;
    --orange: #f7962e;
    --sky: #1d8fcf;
    --backdrop: #ececec;
  }
  * { margin: 0; padding: 0; box-sizing: border-box; }
  html, body { width: 1200px; height: 1200px; overflow: hidden; }
  body {
    background: var(--backdrop);
    font-family: "Ubuntu", sans-serif;
    position: relative;
  }
  .card {
    position: absolute;
    left: 150px;
    width: 900px;
    height: 514px;
    border-radius: 22px;
    overflow: hidden;
    box-shadow: 0 6px 18px rgba(0,0,0,0.22);
    color: var(--orange);
  }
  .card--front {
    top: 50px;
    background: radial-gradient(ellipse at 45% 50%, var(--navy-glow) 0%, var(--navy-mid) 40%, var(--navy-deep) 85%);
  }
  .card--back { top: 636px; background: var(--orange); }

  .card__website {
    position: absolute; top: 34px; left: 40px;
    font-size: 22px; font-weight: 500;
  }
  .brand {
    position: absolute;
    display: flex; align-items: center; gap: 18px;
  }
  .brand__dot {
    border-radius: 50%;
    background: var(--sky);
    flex: none;
  }
  .brand__name { font-weight: 700; color: var(--orange); white-space: nowrap; }

  .card--front .brand { top: 212px; left: 0; width: 100%; justify-content: center; }
  .card--front .brand__dot { width: 72px; height: 72px; }
  .card--front .brand__name { font-size: 58px; }

  .services {
    position: absolute; left: 40px; bottom: 36px;
    list-style: none; font-size: 20px; line-height: 1.3; font-weight: 500;
  }
  .social {
    position: absolute; right: 40px; bottom: 40px;
    font-size: 20px; font-weight: 700; line-height: 1.35;
    display: grid; grid-template-columns: auto auto; column-gap: 22px;
  }

  .back__art { position: absolute; inset: 0; width: 100%; height: 100%; }
  .card--back .brand { top: 48px; left: 40px; }
  .card--back .brand__dot { width: 52px; height: 52px; }
  .card--back .brand__name { font-size: 40px; }
  .contact {
    position: absolute; top: 46px; right: 40px;
    font-size: 24px; line-height: 1.3;
  }
  .contact__name { font-weight: 700; font-size: 26px; }
  .contact__title, .contact__email { font-weight: 500; }
  .card__footer {
    position: absolute; left: 30px; right: 30px; bottom: 28px;
    color: var(--navy-deep); font-size: 17.5px; font-weight: 700;
    white-space: nowrap;
  }
</style>
</head>
<body>

  <section class="card card--front" aria-label="Business card front">
    <p class="card__website">www.brightlanesites.com</p>

    <div class="brand">
      <span class="brand__dot"></span>
      <span class="brand__name">Bright Lane Sites</span>
    </div>

    <ul class="services">
      <li>Web Design</li>
      <li>Website Management</li>
      <li>Internet Marketing</li>
    </ul>

    <div class="social">
      <span>Twitter:</span><span>@brightlanesites</span>
      <span>Facebook:</span><span>www.facebook.com/brightlanesites</span>
    </div>
  </section>

  <section class="card card--back" aria-label="Business card back">
    <svg class="back__art" viewBox="0 0 900 514" preserveAspectRatio="none" aria-hidden="true">
      <defs>
        <radialGradient id="navy-field" cx="0.6" cy="0.4" r="0.7">
          <stop offset="0" stop-color="#1c56a8"/>
          <stop offset="0.45" stop-color="#1f3f92"/>
          <stop offset="1" stop-color="#26236a"/>
        </radialGradient>
      </defs>
      <polygon points="0,0 900,0 900,210 265,345 0,250" fill="url(#navy-field)"/>
    </svg>

    <div class="brand">
      <span class="brand__dot"></span>
      <span class="brand__name">Bright Lane Sites</span>
    </div>

    <div class="contact">
      <p class="contact__name">Mark Pellow</p>
      <p class="contact__title">President/CEO</p>
      <p class="contact__email">mark@brightlanesites.com</p>
    </div>

    <p class="card__footer">Phone: 520-481-7093, Toll Free: 866-481-7093, Address: 4315 E. Kestrel Ave. Ste. 140, Tucson, AZ 85733</p>
  </section>

</body>
</html>
```